Investment company needing business card

We are wanting a business card which looks sharp and easy on the eye. We are thinking of having a business card with the logo embossed on it, to really make it stand out. We will only have a small amount of information of the business card, person's name, position, email address and phone number

Contact Information for Business Card

Danica Pruett
Executive Assistant
+64 21 547 3162
danicap@harwellcapital.co.nz

Requirements
Must have
• Embossed logo
Should not have
• Not to be busy

```html
<!DOCTYPE html>
<html lang="en">
<head>
<meta charset="utf-8">
<title>Harwell Capital – Business Card</title>
<link rel="stylesheet" href="https://fonts.googleapis.com/css2?family=Oswald:wght@500&family=Roboto:wght@400;700&display=swap">
<style>
  :root {
    --backdrop: #2a2a2b;
    --card: #1d1d1e;
    --card-edge: #161617;
    --accent: #21b56f;
    --ink: #f2f2f2;
    --ink-soft: #d9d9d9;
  }
  * { margin: 0; padding: 0; box-sizing: border-box; }
  html, body { width: 1200px; height: 900px; overflow: hidden; }
  body {
    background: var(--backdrop);
    font-family: 'Roboto', Arial, sans-serif;
    position: relative;
  }
  .card {
    position: absolute;
    left: 230px;
    width: 740px;
    height: 380px;
    background: radial-gradient(ellipse at 60% 30%, #262627 0%, var(--card) 70%);
    border-bottom: 7px solid var(--accent);
    box-shadow: 0 10px 24px rgba(0,0,0,0.45);
  }
  .card--front { top: 50px; }
  .card--back { top: 470px; }

  .brand {
    position: absolute;
    top: 50%; left: 50%;
    transform: translate(-50%, -50%);
    display: flex;
    align-items: center;
    gap: 22px;
  }
  .brand__mark {
    width: 64px; height: 64px;
    background: var(--accent);
  }
  .brand__name {
    font-weight: 700;
    font-size: 46px;
    letter-spacing: 3px;
    color: var(--ink);
    line-height: 1;
    text-transform: uppercase;
  }

  .identity {
    position: absolute;
    right: 420px;
    top: 142px;
    text-align: right;
  }
  .identity__name {
    font-family: 'Oswald', 'Arial Narrow', sans-serif;
    font-weight: 500;
    font-size: 40px;
    color: var(--accent);
    line-height: 1;
    letter-spacing: 0.5px;
    text-transform: uppercase;
  }
  .identity__role {
    margin-top: 6px;
    font-size: 17px;
    color: var(--ink);
  }
  .divider {
    position: absolute;
    left: 342px;
    top: 138px;
    width: 2px;
    height: 86px;
    background: var(--accent);
  }
  .contacts {
    position: absolute;
    left: 368px;
    top: 142px;
    list-style: none;
  }
  .contacts li {
    display: flex;
    align-items: center;
    gap: 12px;
    font-size: 17px;
    color: var(--ink-soft);
    height: 27px;
  }
  .contacts svg { width: 14px; height: 14px; flex: none; }
</style>
</head>
<body>
  <section class="card card--front">
    <div class="brand">
      <div class="brand__mark"></div>
      <div class="brand__name">Harwell Capital</div>
    </div>
  </section>

  <section class="card card--back">
    <div class="identity">
      <div class="identity__name">Danica Pruett</div>
      <div class="identity__role">Executive Assistant</div>
    </div>
    <div class="divider"></div>
    <ul class="contacts">
      <li>
        <svg viewBox="0 0 16 16" aria-hidden="true"><path d="M4 1.5l2.3 3-1.4 1.6c.8 1.9 2.3 3.4 4.2 4.3l1.6-1.4 3 2.3-1.3 2.6C7.2 13.6 2.4 8.8 1.5 3.2z" fill="#21b56f"/></svg>
        +64 21 547 3162
      </li>
      <li>
        <svg viewBox="0 0 16 16" aria-hidden="true"><rect x="1.5" y="3.5" width="13" height="9" fill="none" stroke="#21b56f" stroke-width="1.4"/><path d="M1.5 3.8L8 9l6.5-5.2" fill="none" stroke="#21b56f" stroke-width="1.4"/></svg>
        danicap@harwellcapital.co.nz
      </li>
      <li>
        <svg viewBox="0 0 16 16" aria-hidden="true"><g fill="none" stroke="#21b56f" stroke-width="1.3"><circle cx="8" cy="8" r="6.3"/><ellipse cx="8" cy="8" rx="2.8" ry="6.3"/><path d="M1.8 8h12.4"/></g></svg>
        www.harwellcapital.co.nz
      </li>
    </ul>
  </section>
</body>
</html>
```